Amber Willow Intimates

The site is an Adult Retail Store website that sells products. There will be a Splash Page and inside (Home Page). The Splash page will have normal warning to users that 18+ material is inside. The splash page will contain....

- Lady (logo)
- disclaimer link for under 18
- enter and exit buttons
- Other detail in the must have

The client has also asked that this Splash Page must set the tone for the whole site and encourage users to enter. The client would like to give a feeling of romance, beauty, elegance, classy, inviting. The client would like to move away from the stigma associated with Adult stores as “sleezy” and create a welcoming feel for both males and females.

Also an internal Home Page will be created for the website which will take the same look and feel as the Splash Page. There will be a graphic header using some of the images below. Once the Home Page has been designer there will be minor colour background changes to the internal Home Page for the 2 Shop Pages (See Below).

Amber Willow is the largest adult store in Adelaide and will be using this website primarily to sell their products online.

Target Market(s)

Described as a “his and hers adult store” Amber Willow focuses on both males and females over the age of 18.

Requirements
Must have
• Amber Willows three main colours are Black, Purple and White. Please refer to current site for exact values.
• Also various gradients of these colours are encouraged to bring the website up to date with modern trends. The current website www.amberwillowintimates-example.com.au is very outdated!
• They would like the Lady larger and on the left of the Splash Page and an Enter Site on the Splash Page. They do not like the gothic font as such however they still want a softer gothic feel and appeal. The client quite likes the use of Trajan Pro font. I have attached a concept they quite liked to give an idea of the direction they would like to head in. This is by no means a suggested look and client is open to more suggestions. They would like to see some attention paid to modifying the lady to bring it up to date.
• The client has suggested a shining moon and some stars in the background of the Splash Page. Here the “under 18” content disclaimer link needs to be put discretely down the bottom of the Splash Page. The woman’s head will eventually be a Flash file which will have her hair flowing.
• When the visitor clicks through the Enter Site they will be shown the inside Home Page of the site with a similar feel to the Splash Page and contain typical menu links such as “about us” and “contact us”. On the Home Page there will be 2 doors “His” and “Hers” where the visitor will click through to the Shop. They like the idea of open doors to enter through. Both “His” and “Hers” shop pages will have the same theme as the Home Page with a minor change in the background. Possibly a darker colour for the males side and a lighter side for the females.
• The client has hand-picked the following images from pixmarta-example.com. These may be used in the design of the Home Page at the designers discretion. Other similar images can be used to achieve the feel.
• (please search numbers at www.pixmarta-example.com for thumbnails)
• #3520947
• #6084213
• #7193052
• #8305271
• #1047389
• #2658140
• If designer can also create the Flash component there will be an extra $300 paid. Please let us know.
Nice to have
• Whilst not part of the web design component here it will be of great use if designer had flash skills. This website requires some flash animation on the logo in the Splash Page and header of the Home Page that would require woman’s hair to flow so some ongoing work could be possible for winning designer.
Should not have
• Client has made the comment that they don’t want the site to be “boring and flat”

```html
<!DOCTYPE html>
<html lang="en">
<head>
<meta charset="utf-8">
<title>Amber Willow Intimates — Splash</title>
<link rel="stylesheet" href="https://fonts.googleapis.com/css2?family=Cinzel:wght@400;600&display=swap">
<style>
  :root {
    --sky-top: #3a0f52;
    --sky-mid: #8a2ab0;
    --sky-low: #5a1580;
    --horizon: #2a0e33;
    --floor: #350a4a;
    --ground-dark: #1b1a1d;
    --ink: #0b0510;
    --lilac: #e2c7ec;
    --text-pink: #c77fd8;
    --panel-line: #4d2a59;
    --btn-top: #a14db8;
    --btn-bottom: #7d0f94;
    --btn-text: #f6ecf8;
  }
  * { box-sizing: border-box; margin: 0; padding: 0; }
  html, body { width: 1200px; height: 928px; overflow: hidden; background: var(--ground-dark); }
  .splash {
    position: relative; width: 1200px; height: 928px; overflow: hidden;
    background: linear-gradient(180deg, var(--floor) 581px, #2c0c3b 700px, #221628 800px, var(--ground-dark) 928px);
    font-family: "Cinzel", "Trajan Pro", serif;
  }
  .night-sky {
    position: absolute; left: 0; top: 0; width: 1200px; height: 581px;
    background:
      radial-gradient(ellipse 70px 70px at 679px 195px, rgba(240,225,245,0.9), rgba(240,225,245,0) 70%),
      radial-gradient(ellipse 520px 120px at 520px 120px, rgba(214,170,224,0.55), rgba(214,170,224,0) 70%),
      linear-gradient(180deg, var(--sky-top) 0%, var(--sky-mid) 30%, var(--sky-low) 60%, #3a1045 82%, var(--horizon) 100%);
  }
  .night-sky::after {
    content: ""; position: absolute; inset: 0;
    background: linear-gradient(90deg, rgba(0,0,0,0.55) 0%, rgba(0,0,0,0) 30%, rgba(0,0,0,0) 75%, rgba(0,0,0,0.45) 100%);
  }
  .horizon-line {
    position: absolute; left: 0; top: 580px; width: 1200px; height: 1px; background: #5b2b6b;
  }
  .lady-figure {
    position: absolute; left: 165px; top: 277px; width: 220px; height: 370px;
    background: linear-gradient(180deg, #120818 0%, #07030a 100%);
    border-radius: 90px 90px 16px 16px;
    box-shadow: 0 0 6px rgba(200,140,220,0.5);
  }
  .brand {
    position: absolute; left: 411px; top: 265px;
  }
  .brand-name {
    font-family: "Cinzel", serif; font-weight: 400; font-size: 51px; line-height: 66px;
    color: var(--ink); letter-spacing: 1px; text-transform: uppercase; white-space: nowrap;
  }
  .brand-tagline {
    margin-top: 0; font-family: "Cinzel", serif; font-weight: 400; font-size: 22.5px; line-height: 28px;
    color: var(--lilac); text-transform: uppercase; letter-spacing: 0.5px; white-space: nowrap;
  }
  .age-gate {
    position: absolute; left: 131px; top: 666px; width: 938px; height: 157px;
    border: 1px solid var(--panel-line);
    background: linear-gradient(180deg, rgba(40,10,50,0.6), rgba(30,20,34,0.4));
  }
  .age-gate-notice {
    position: absolute; left: 0; top: 12px; width: 100%; text-align: center; white-space: nowrap;
    font-family: Verdana, Geneva, "DejaVu Sans", sans-serif; font-size: 12px; color: var(--text-pink);
  }
  .age-gate-notice strong { font-weight: 700; margin-left: 4px; }
  .gate-button {
    position: absolute; top: 55px; width: 271px; height: 52px;
    border-radius: 6px; border: 1px solid #3b0d47;
    background: linear-gradient(180deg, var(--btn-top) 0%, #8f33a8 45%, var(--btn-bottom) 55%, #8a1aa0 100%);
    box-shadow: 0 1px 3px rgba(0,0,0,0.6);
    color: var(--btn-text); font-family: "Cinzel", serif; font-size: 27px; font-weight: 400;
    text-align: center; line-height: 52px; text-decoration: none; white-space: nowrap;
  }
  .gate-button::after {
    content: ""; position: absolute; left: 0; top: 54px; width: 100%; height: 30px; border-radius: 6px;
    background: linear-gradient(180deg, rgba(140,70,160,0.35), rgba(140,70,160,0));
  }
  .gate-button--leave { left: 172px; }
  .gate-button--enter { left: 464px; top: 57px; }
</style>
</head>
<body>
<main class="splash">
  <div class="night-sky" role="img" aria-label="Violet night sky with a full moon and drifting clouds"></div>
  <div class="horizon-line"></div>
  <div class="lady-figure" role="img" aria-label="Silhouette of a lady holding a whip, standing on the horizon"></div>

  <header class="brand">
    <h1 class="brand-name">Amber Willow<br>Intimates</h1>
    <p class="brand-tagline">His &amp; Hers Adult Shop</p>
  </header>

  <section class="age-gate">
    <p class="age-gate-notice">Contents of this website may contain explicit materials which may offend some people. This website is designed for Mature Audiences <strong>18+</strong> .</p>
    <a class="gate-button gate-button--leave" href="#">Leave This Site</a>
    <a class="gate-button gate-button--enter" href="#">Enter Site</a>
  </section>
</main>
</body>
</html>
```